Heart centered conscious skincare product maker needs mindful designer to tweak or change deodorant

Heart centered conscious skincare product maker needs mindful designer to tweak or change the roll on deodorant label (58x120mm) and design the box (40x40x108mm) it fits inside. This is a new product, I have created the label in Canva but it could use some professional eyes to tweak or change completely as appropriately convey and entice. Either way, I need a simple standing rectangle box that it will fit into with all the required (FDA) info. This product will be selling on Corvella so appropriate first impressions is vital. I'll have 3 more products to follow this one so the opportunity for more creative fun is available.

I will give you the final barcode soon, it is not the same one I've used on my current sample sticker.

The last attached picture of my current bottle in the grass has a thread bracelet around it that has been blessed my a balinese priest for intentions of courage, strength,love and abundance. It is our gift to our customers and is to be worn on their wrist.

Target Market(s)

USA women & men 22-54, vegan, yogis, vegetarians, organic consumers, health conscious,

Industry/Entity Type

Product

Requirements
Must have
• Professional & smart. Please show sticker design on bottle (amber bottle with black top) and with the box standing next to it at an angle and with white background.
Nice to have
• Feel free to change the colors if needed. I'm open to have white on black or black on white.. or something even more fresh like an aqua (ocean) or green (deep forest).

```html
<!DOCTYPE html>
<html lang="en">
<head>
<meta charset="utf-8">
<title>Serawa Deodorant – Box and Label</title>
<link rel="stylesheet" href="https://fonts.googleapis.com/css2?family=Barlow:wght@400;500;600&family=Barlow+Condensed:wght@400;500&family=Libre+Baskerville:ital@1&display=swap">
<style>
  :root {
    --charcoal: #4a4644;
    --charcoal-deep: #3c3937;
    --gold: #c9972a;
    --cream: #f4f1ec;
    --muted: #8d8783;
    --faint: #5e5956;
    --page: #ffffff;
  }
  * { box-sizing: border-box; margin: 0; padding: 0; }
  html, body { width: 1200px; height: 1000px; overflow: hidden; background: var(--page); }
  .canvas { position: relative; width: 1200px; height: 1000px; font-family: "Barlow", sans-serif; }

  /* ---------- brand name (plain wordmark) ---------- */
  .brand {
    position: absolute; display: flex; align-items: center; gap: 12px;
    color: var(--gold); font-family: "Barlow", sans-serif; font-weight: 500;
    letter-spacing: 4px; white-space: nowrap;
  }
  .brand-dot { display: block; border-radius: 50%; background: var(--gold); flex: none; }

  /* ---------- box: side panel ---------- */
  .box-side {
    position: absolute; left: 170px; top: 90px; width: 200px; height: 800px;
    background: var(--charcoal-deep); color: var(--muted);
    border-bottom: 14px solid var(--gold);
  }
  .ingredients { position: absolute; left: 24px; right: 24px; top: 130px; }
  .ingredients-title {
    font-family: "Barlow Condensed", sans-serif; font-size: 13px; letter-spacing: 1px;
    text-align: center; margin-bottom: 14px; text-transform: uppercase;
  }
  .ingredients-list {
    font-family: "Barlow Condensed", sans-serif; font-size: 12px; line-height: 2.6;
    text-align: center;
  }
  .side-brand {
    position: absolute; left: 0; right: 0; top: 570px; text-align: center;
    color: var(--faint); font-size: 20px; font-weight: 500; letter-spacing: 3px;
  }
  .side-url {
    position: absolute; left: 0; right: 0; bottom: 40px; text-align: center;
    font-size: 9px; letter-spacing: 1px; color: #6a6461;
  }

  /* ---------- box: front panel ---------- */
  .box-front {
    position: absolute; left: 370px; top: 90px; width: 290px; height: 800px;
    background: linear-gradient(160deg, #5a5553 0%, var(--charcoal) 45%, var(--charcoal-deep) 100%);
    color: var(--cream);
    border-bottom: 14px solid var(--gold);
  }
  .box-front .brand { left: 22px; top: 150px; font-size: 34px; }
  .box-front .brand-dot { width: 22px; height: 22px; }
  .tagline {
    position: absolute; left: 22px; top: 282px;
    font-family: "Libre Baskerville", serif; font-style: italic; font-size: 14px;
  }
  .product-title {
    position: absolute; left: 22px; top: 332px;
    font-size: 30px; font-weight: 500; letter-spacing: 5px; color: var(--gold);
  }
  .product-scent {
    position: absolute; left: 22px; top: 374px; font-size: 15px; font-weight: 500; letter-spacing: 0.5px;
  }
  .unisex-icon { position: absolute; left: 28px; top: 412px; width: 120px; height: 70px; }
  .rule { position: absolute; left: 22px; right: 40px; height: 1px; background: var(--gold); }
  .rule.top { top: 510px; }
  .rule.bottom { top: 715px; }
  .claims { position: absolute; left: 22px; top: 538px; list-style: none; }
  .claims li { font-size: 16px; letter-spacing: 1.5px; line-height: 32px; }
  .net { position: absolute; left: 22px; top: 748px; font-size: 13px; font-weight: 500; }
  .url { position: absolute; right: 40px; top: 748px; font-size: 10px; letter-spacing: 1.5px; }

  /* ---------- bottle label ---------- */
  .label {
    position: absolute; left: 740px; top: 300px; width: 250px; height: 420px;
    background: var(--charcoal); color: var(--cream);
    border-bottom: 12px solid var(--gold);
  }
  .label .brand { left: 20px; top: 90px; font-size: 25px; gap: 9px; letter-spacing: 3px; }
  .label .brand-dot { width: 16px; height: 16px; }
  .label .tagline { left: 20px; top: 186px; font-size: 10.5px; }
  .label .product-title { left: 20px; top: 214px; font-size: 21px; letter-spacing: 3.5px; }
  .label .product-scent { left: 20px; top: 244px; font-size: 11px; }
  .label .unisex-icon { left: 24px; top: 268px; width: 80px; height: 46px; }
  .label .rule.top { top: 330px; left: 20px; right: 20px; }
  .label-claims { position: absolute; left: 20px; top: 344px; list-style: none; }
  .label-claims li { font-size: 9.5px; letter-spacing: 0.8px; line-height: 15px; }
  .label-net { position: absolute; left: 20px; top: 392px; font-size: 8px; color: var(--gold); font-weight: 600; }
</style>
</head>
<body>
<main class="canvas">

  <section class="box-side">
    <div class="ingredients">
      <p class="ingredients-title">Ingredients</p>
      <p class="ingredients-list">Water, Maltitol (Sweetener), Glucose, Mango Juice, Mango Flavor, Citric Acid (pH Adjuster), Dextrin (Bulking Agent), Locust Bean Gum, Potassium Chloride (Thickener), Glycine, Alpinia, Maripuri Agalactia, Glutathione, Hesperidin, Vitamin B1, Vitamin B6</p>
    </div>
    <p class="side-brand">SERAWA</p>
    <p class="side-url">www.serawa.com</p>
  </section>

  <section class="box-front">
    <p class="brand"><span class="brand-dot"></span>SERAWA</p>
    <p class="tagline">100% Vegan &amp; 100% Amazing</p>
    <h1 class="product-title">DEODORANT</h1>
    <p class="product-scent">PEPPERMINT &amp; LAVENDER</p>
    <svg class="unisex-icon" viewBox="0 0 120 70" fill="none" stroke="#c9972a" stroke-width="4" aria-label="Unisex symbol">
      <circle cx="38" cy="32" r="20"/>
      <circle cx="64" cy="32" r="20"/>
      <line x1="24" y1="46" x2="10" y2="62"/>
      <line x1="8" y1="52" x2="22" y2="64"/>
      <line x1="84" y1="32" x2="108" y2="32"/>
      <polyline points="100,24 108,32 100,40"/>
    </svg>
    <div class="rule top"></div>
    <ul class="claims">
      <li>100% Natural</li>
      <li>Organic Ingredients</li>
      <li>No Aluminum</li>
      <li>No Synthethic Fragrance</li>
      <li>Bicarbonate Free</li>
    </ul>
    <div class="rule bottom"></div>
    <p class="net">Net Wt. 50mL</p>
    <p class="url">www.serawa.com</p>
  </section>

  <section class="label">
    <p class="brand"><span class="brand-dot"></span>SERAWA</p>
    <p class="tagline">100% Vegan &amp; 100% Amazing</p>
    <h2 class="product-title">DEODORANT</h2>
    <p class="product-scent">PEPPERMINT &amp; LAVENDER</p>
    <svg class="unisex-icon" viewBox="0 0 120 70" fill="none" stroke="#c9972a" stroke-width="5" aria-label="Unisex symbol">
      <circle cx="38" cy="32" r="20"/>
      <circle cx="64" cy="32" r="20"/>
      <line x1="24" y1="46" x2="10" y2="62"/>
      <line x1="8" y1="52" x2="22" y2="64"/>
      <line x1="84" y1="32" x2="108" y2="32"/>
      <polyline points="100,24 108,32 100,40"/>
    </svg>
    <div class="rule top"></div>
    <ul class="label-claims">
      <li>100% Natural · Bicarbonate Free</li>
      <li>Organic Ingredients · No Aluminum</li>
      <li>No Synthetic Fragrance</li>
    </ul>
    <p class="label-net">Net Wt. 50mL</p>
  </section>

</main>
</body>
</html>
```